Illustrations for a Project Management Concept

we need illustrations for 5 project management principles that make up a holistic approach to project management, without all the BS. if we extract all the methodology, system, tool and mumbo-jumbo out of project management, we end up with some essential principles that are simple to understand and use. It's likely that people who use them will not be traditional Project Management types.

I've mocked up something that looks very corporate based on a template, but this has the wrong tone; the wrong feeling. I'd like something "funky" and colorful that conveys "Action" within "Simplicity".

the PPT file with the dark-blue background is the "corporate" consulting type mockup. the PPT with the white background shows an idea I had for breaking out each of the 5 principles (only one shown) to make it larger, with some text in a callout.

In the final deliverable, I need to be able to both show all 5 on one diagram, as well as slicing the image to display each principle separately. i do not have editing capabilities for vector image formats, only image formats

Reason: there are a number of designers who have only just accepted the invitation. I want to give everyone a chance to submit.

```html
<!DOCTYPE html>
<html lang="en">
<head>
<meta charset="utf-8">
<title>Achieve Outcomes – 5 Principles</title>
<link rel="stylesheet" href="https://fonts.googleapis.com/css2?family=Jost:wght@400;500&display=swap">
<style>
  :root {
    --bg-orange: #ff6600;
    --halo-orange: #ff8500;
    --halo-ring: #ff9a3c;
    --core-orange: #e8841c;
    --core-ring: #f59a3a;
    --hub-shadow: #e6e6e6;
    --hub-pink: #ff99cc;
    --white: #ffffff;
    --ink: #2e2e33;
    --value-green: #b3dcb4;
    --models-blue: #66dcfb;
    --threats-teal: #99cccc;
    --entropy-salmon: #f49191;
  }
  html, body {
    margin: 0;
    padding: 0;
    width: 1200px;
    height: 834px;
    overflow: hidden;
    background: var(--bg-orange);
  }
  .principles-diagram {
    display: block;
    width: 1200px;
    height: 834px;
    font-family: "Jost", "Futura", sans-serif;
  }
  .halo { fill: var(--halo-orange); stroke: var(--halo-ring); stroke-width: 12; }
  .core { fill: var(--core-orange); stroke: var(--core-ring); stroke-width: 10; }
  .hub-shadow { fill: var(--hub-shadow); opacity: 0.92; }
  .connector { fill: var(--white); }
  .hub { fill: var(--hub-pink); stroke: var(--white); stroke-width: 9; }
  .node { stroke: var(--white); stroke-width: 11; }
  .node--value { fill: var(--value-green); }
  .node--models { fill: var(--models-blue); }
  .node--threats { fill: var(--threats-teal); }
  .node--entropy { fill: var(--entropy-salmon); }
  .hub-title { fill: var(--ink); font-size: 43px; font-weight: 500; text-anchor: middle; }
  .hub-subtitle { fill: var(--white); font-size: 22px; font-weight: 400; text-anchor: middle; }
  .node-label { fill: var(--ink); font-size: 25px; font-weight: 400; text-anchor: middle; }
</style>
</head>
<body>
<svg class="principles-diagram" viewBox="0 0 1200 834" xmlns="http://www.w3.org/2000/svg" role="img" aria-label="Achieve Outcomes: 5 Principles diagram">
  <rect width="1200" height="834" fill="var(--bg-orange)"/>

  <!-- concentric backdrop -->
  <circle class="halo" cx="609" cy="400" r="323"/>
  <circle class="core" cx="609" cy="400" r="205"/>
  <circle class="hub-shadow" cx="609" cy="400" r="170"/>

  <!-- connectors -->
  <path class="connector" d="M318,240 Q420,280 505,300 L490,338 Q400,310 300,290 Z"/>
  <path class="connector" d="M888,230 Q800,280 712,300 L728,338 Q820,300 918,285 Z"/>
  <path class="connector" d="M310,530 Q410,490 500,460 L515,500 Q430,560 360,585 Z"/>
  <path class="connector" d="M900,540 Q800,500 715,465 L700,503 Q790,560 860,590 Z"/>

  <!-- hub -->
  <circle class="hub" cx="609" cy="400" r="148"/>
  <text class="hub-title" x="612" y="385">Achieve</text>
  <text class="hub-title" x="612" y="428">Outcomes</text>
  <text class="hub-subtitle" x="606" y="469">5 Principles</text>

  <!-- principle nodes -->
  <g class="principle">
    <circle class="node node--value" cx="276" cy="194" r="100"/>
    <text class="node-label" x="276" y="166">Fulfill</text>
    <text class="node-label" x="276" y="197">Customer</text>
    <text class="node-label" x="276" y="228">Value</text>
  </g>
  <g class="principle">
    <circle class="node node--models" cx="940" cy="196" r="100"/>
    <text class="node-label" x="940" y="170">Build</text>
    <text class="node-label" x="940" y="203">Shared</text>
    <text class="node-label" x="940" y="236">Models</text>
  </g>
  <g class="principle">
    <circle class="node node--threats" cx="275" cy="615" r="100"/>
    <text class="node-label" x="275" y="592">Eliminate</text>
    <text class="node-label" x="275" y="624">Teaming</text>
    <text class="node-label" x="275" y="656">Threats</text>
  </g>
  <g class="principle">
    <circle class="node node--entropy" cx="936" cy="612" r="100"/>
    <text class="node-label" x="936" y="606">Suppress</text>
    <text class="node-label" x="936" y="639">Entropy</text>
  </g>
</svg>
</body>
</html>
```